New management consulting website

I need a 4-5 page website that I can manage in WordPress on Hostlane.example for a new management consulting company. The website is www.torvik-example.com and the company name is Torvik Group LLC. The attached spec has an example of a draft site, layout and actual copy and includes company and contact information. I have more high-res images I can send.

Must include instruction/assistance loading the site to my WordPress dashboard.

Target Market(s)

Any business, especially SAAS

Industry/Entity Type

Consultant

Coding

Coded - Design and coding required

Number of Pages Required

4 page

Font styles to use
Sans Serif

Colors
0456a4

Requirements
Must have
• Modern and stylish

```html
<!DOCTYPE html>
<html lang="en">
<head>
<meta charset="utf-8">
<title>Torvik Consulting — Management Consulting Company</title>
<link href="https://fonts.googleapis.com/css2?family=Poppins:wght@300;400;500;600;700;800&display=swap" rel="stylesheet">
<style>
:root{
  --navy:#1d3f72;
  --navy-deep:#16335e;
  --ink:#2b2b2b;
  --text:#555b66;
  --dark:#262626;
  --card:#2a2a2a;
  --hero:#0b1824;
  --lilac:#c9cedf;
  --white:#ffffff;
  --line:#d7d9de;
}
*{box-sizing:border-box;margin:0;padding:0}
html,body{width:1200px;height:3829px;overflow:hidden}
body{position:relative;font-family:'Poppins',sans-serif;background:var(--white);color:var(--ink)}
.abs{position:absolute}
a{color:inherit;text-decoration:none}

/* header */
.site-header{position:absolute;left:0;top:0;width:1200px;height:72px;background:var(--white);z-index:5}
.brand{position:absolute;left:152px;top:18px;font-size:26px;font-weight:600;color:var(--navy);letter-spacing:1px;line-height:36px;font-family:'Poppins',sans-serif}
.main-nav a{position:absolute;top:22px;font-size:15px;color:#333}
.main-nav .active{border-bottom:2px solid var(--navy);padding-bottom:6px}
.btn-contact{position:absolute;left:919px;top:15px;width:129px;height:37px;border-radius:19px;background:var(--navy);color:#fff;font-size:15px;font-weight:500;display:flex;align-items:center;justify-content:center}

/* hero */
.hero{position:absolute;left:0;top:71px;width:1200px;height:760px}
.hero-bg{position:absolute;inset:0}
.hero-title{position:absolute;left:0;width:1200px;top:218px;text-align:center;color:#fff;font-size:45px;font-weight:800;letter-spacing:-1px}
.hero-sub{position:absolute;left:0;width:1200px;top:276px;text-align:center;color:#fff;font-size:21px;font-weight:400}
.btn-pill{position:absolute;top:338px;height:40px;border-radius:20px;font-size:13px;font-weight:600;display:flex;align-items:center;justify-content:center}
.btn-start{left:461px;width:131px;background:var(--navy);color:#fff}
.btn-learn{left:607px;width:132px;background:#fff;color:var(--ink)}
.hero-badge{position:absolute;left:561px;top:577px;width:80px;height:80px;border-radius:50%;background:#fff;box-shadow:0 2px 10px rgba(0,0,0,.25)}

/* about */
.eyebrow{position:absolute;left:150px;top:866px;font-size:20px;color:var(--navy)}
.about-title{position:absolute;left:150px;top:898px;font-size:27px;font-weight:700;line-height:39px;color:var(--ink);width:460px}
.about-text{position:absolute;left:150px;top:986px;width:450px;font-size:13.4px;line-height:24px;color:var(--text)}
.btn-about{position:absolute;left:150px;top:1158px;width:159px;height:39px;border-radius:20px;background:var(--navy);color:#fff;font-size:13px;font-weight:600;display:flex;align-items:center;justify-content:center}
.photo{position:absolute}

/* services */
.services-bg{position:absolute;left:0;top:1250px;width:1200px;height:1200px}
.section-title{position:absolute;left:0;width:1200px;text-align:center;font-size:32px;font-weight:400;color:var(--ink)}
.section-title strong{font-weight:700;color:var(--navy)}
.services-lead{position:absolute;left:320px;top:1545px;width:560px;text-align:center;font-size:13.4px;line-height:23px;color:var(--navy)}
.service-card{position:absolute;width:284px;height:277px;background:var(--card);border:1px solid #111;color:#fff;text-align:center}
.service-card.featured{background:var(--navy)}
.service-card svg.icon{position:absolute;left:112px;top:22px;width:60px;height:64px}
.service-card .divider{position:absolute;left:62px;top:106px;width:160px;height:1px;background:linear-gradient(90deg,transparent,#8a8f99,transparent)}
.service-card .divider::after{content:"";position:absolute;left:78px;top:-2px;width:5px;height:5px;border-radius:50%;background:#fff}
.service-card h3{position:absolute;left:0;width:100%;top:127px;font-size:15.5px;font-weight:600}
.service-card p{position:absolute;left:22px;width:240px;top:160px;font-size:12.4px;line-height:21px;color:#e6e6e6}
.service-card .more{position:absolute;left:0;width:100%;top:230px;font-size:12px;color:#7f9cd0}
.service-card .more span{border-bottom:1px solid #7f9cd0}
.service-card.featured .more{color:#fff}
.service-card.featured .more span{border-color:#fff}
.corner-mark{position:absolute;right:18px;bottom:14px;width:14px;height:14px;border:1.5px solid #fff}

/* team */
.title-rule{position:absolute;left:572px;top:2513px;width:60px;height:3px;background:var(--navy)}
.team-text{position:absolute;left:229px;top:2581px;width:340px;font-size:12.8px;line-height:21px;color:var(--navy)}
.team-text p{margin-bottom:8px}
.team-photo{position:absolute;left:661px;top:2535px;width:254px;height:254px;border-radius:50%;border:2px solid #8c97b0;overflow:hidden}

/* contact */
.contact-card{position:absolute;left:351px;top:2903px;width:697px;height:529px;background:#fff;box-shadow:0 4px 24px rgba(0,0,0,.12)}
.contact-title{position:absolute;left:406px;top:2948px;font-size:29px;font-weight:400;color:var(--ink)}
.contact-title strong{color:var(--navy);font-weight:700}
.consent-box{position:absolute;left:406px;top:3010px;width:16px;height:16px;border:1px solid #aaa;border-radius:2px}
.consent{position:absolute;left:439px;top:3007px;width:570px;font-size:10.6px;line-height:18px;color:#555}
.field label{position:absolute;font-size:10.5px;font-weight:500;color:#333}
.field label sup{font-size:8px}
.field .val{position:absolute;font-size:12px;color:#9a9a9a}
.field .rule{position:absolute;height:1px;background:var(--line)}
.send-btn{position:absolute;left:909px;top:3331px;width:62px;height:62px;border-radius:50%;background:var(--navy)}

/* footer */
.footer{position:absolute;left:0;top:3470px;width:1200px;height:359px}
.footer-brand{position:absolute;left:0;width:1200px;top:127px;text-align:center;font-size:44px;font-weight:600;color:var(--navy);letter-spacing:2px}
.footer-nav a{position:absolute;top:3690px;font-size:15.5px;color:#fff}
.copyright{position:absolute;left:174px;top:3778px;font-size:12.4px;color:#ddd}
.social{position:absolute;top:3773px;width:29px;height:29px;border-radius:50%;background:var(--navy)}
.legal{position:absolute;left:797px;top:3779px;font-size:11.5px;color:#ddd}
.legal span{margin:0 10px;color:#999}
</style>
</head>
<body>

<header class="site-header">
  <a class="brand" href="#">Torvik Consulting</a>
  <nav class="main-nav">
    <a class="active" href="#" style="left:641px">Home</a>
    <a href="#" style="left:729px">About</a>
    <a href="#" style="left:815px">Services</a>
  </nav>
  <a class="btn-contact" href="#">Contact Us</a>
</header>

<section class="hero">
  <svg class="hero-bg" width="1200" height="760" viewBox="0 0 1200 760">
    <defs>
      <radialGradient id="heroGlow" cx="0.48" cy="0.38" r="0.6">
        <stop offset="0" stop-color="#2f6f86"/>
        <stop offset="0.45" stop-color="#143043"/>
        <stop offset="1" stop-color="#070f18"/>
      </radialGradient>
    </defs>
    <polygon points="0,0 1200,0 1200,575 0,684" fill="url(#heroGlow)" role="img" aria-label="Dark blue network globe with connected user icons and a reaching hand"/>
    <polygon points="0,684 1200,575 1200,760 0,760" fill="#fff"/>
    <polygon points="560,655 1200,575 1200,750" fill="var(--navy)"/>
  </svg>
  <h1 class="hero-title">TORVIK CONSULTING</h1>
  <p class="hero-sub">MANAGEMENT CONSULTING COMPANY</p>
  <a class="btn-pill btn-start" href="#">GET STARTED</a>
  <a class="btn-pill btn-learn" href="#">LEARN MORE</a>
  <div class="hero-badge"></div>
</section>

<section class="about">
  <p class="eyebrow">About Us</p>
  <h2 class="about-title">LOREM IPSUM IS SIMPLY DUMMY TEXT OF THE PRINTING</h2>
  <p class="about-text">Lorem Ipsum is simply dummy text of the printing and typesetting industry. Lorem Ipsum has been the industry's standard dummy text ever since the 1500s, when an unknown printer took a galley of type and scrambled it to make a type specimen book. It has survived not only five centuries, but also the leap into electronic typesetting, remaining essentially unchanged.</p>
  <a class="btn-about" href="#">MORE ABOUT US</a>
  <div class="photo" role="img" aria-label="Black and white photo of colleagues working in an office" style="left:730px;top:846px;width:320px;height:311px;background:linear-gradient(135deg,#6a6a6a,#c9c9c9 55%,#8a8a8a)"></div>
  <div class="photo" role="img" aria-label="Hands typing on a laptop showing the company name" style="left:663px;top:906px;width:307px;height:270px;background:linear-gradient(150deg,#8a6a4e,#3e4a5c 55%,#1e2632);box-shadow:0 2px 8px rgba(0,0,0,.2)"></div>
</section>

<section class="services">
  <svg class="services-bg" width="1200" height="1200" viewBox="0 1250 1200 1200">
    <defs>
      <linearGradient id="lilac" x1="0" y1="0" x2="1" y2="1">
        <stop offset="0" stop-color="#b9c1d8"/>
        <stop offset="0.5" stop-color="#cfd3e2"/>
        <stop offset="1" stop-color="#c6cadb"/>
      </linearGradient>
    </defs>
    <polygon points="0,1435 1200,1326 1200,2320 0,2439" fill="url(#lilac)" role="img" aria-label="Faint technology network background with a wireless signal"/>
    <polygon points="0,1261 1200,1326 0,1435" fill="var(--navy)"/>
  </svg>
  <h2 class="section-title" style="top:1470px">WHAT <strong>WE PROVIDE</strong></h2>
  <p class="services-lead">Lorem Ipsum is simply dummy text of the printing and typesetting industry. Lorem Ipsum has been the industry's standard dummy text .</p>

  <article class="service-card" style="left:150px;top:1627px">
    <svg class="icon" viewBox="0 0 60 64" fill="none" stroke="#fff" stroke-width="2"><circle cx="36" cy="26" r="14"/><circle cx="36" cy="26" r="7"/><path d="M10 54l18-18M14 40l-6 6M24 50l-6 6"/></svg>
    <div class="divider"></div>
    <h3>STRATEGY &amp; OPERATION</h3>
    <p>Lorem Ipsum is simply dummy text of the printing and typesetting industry. Lorem Ipsum has been.</p>
    <a class="more" href="#"><span>LEARN MORE</span></a>
  </article>
  <article class="service-card featured" style="left:458px;top:1627px">
    <svg class="icon" viewBox="0 0 60 64" fill="none" stroke="#fff" stroke-width="2"><path d="M22 24a8 8 0 0 1 8-12 10 10 0 0 1 18 4 7 7 0 0 1-2 13H24a6 6 0 0 1-2-5z"/><path d="M36 30v10"/><rect x="8" y="38" width="10" height="18"/><path d="M18 50h14l14-8"/></svg>
    <div class="divider"></div>
    <h3>DATA ANALYSIS &amp; INSIGHTS</h3>
    <p>Lorem Ipsum is simply dummy text of the printing and typesetting industry. Lorem Ipsum has been.</p>
    <a class="more" href="#"><span>LEARN MORE</span></a>
    <div class="corner-mark"></div>
  </article>
  <article class="service-card" style="left:766px;top:1627px">
    <svg class="icon" viewBox="0 0 60 64" fill="none" stroke="#fff" stroke-width="2"><rect x="18" y="8" width="24" height="16"/><circle cx="12" cy="30" r="5"/><circle cx="48" cy="30" r="5"/><path d="M6 56V40h12M54 56V40H42M20 36h20v8H20zM30 44v12"/></svg>
    <div class="divider"></div>
    <h3>LEADERSHIP DEVELOPMENT</h3>
    <p>Lorem Ipsum is simply dummy text of the printing and typesetting industry. Lorem Ipsum has been.</p>
    <a class="more" href="#"><span>LEARN MORE</span></a>
  </article>

  <article class="service-card" style="left:150px;top:1930px">
    <svg class="icon" viewBox="0 0 60 64" fill="none" stroke="#fff" stroke-width="2"><circle cx="30" cy="16" r="8"/><path d="M30 24v8M14 32h32M14 32v6M30 32v6M46 32v6"/><circle cx="14" cy="44" r="4"/><circle cx="30" cy="44" r="4"/><circle cx="46" cy="44" r="4"/><path d="M7 58a7 7 0 0 1 14 0M23 58a7 7 0 0 1 14 0M39 58a7 7 0 0 1 14 0"/></svg>
    <div class="divider"></div>
    <h3>EXCUTIVE LEADERSHIP</h3>
    <p>Lorem Ipsum is simply dummy text of the printing and typesetting industry. Lorem Ipsum has been.</p>
    <a class="more" href="#"><span>LEARN MORE</span></a>
  </article>
  <article class="service-card" style="left:458px;top:1930px">
    <svg class="icon" viewBox="0 0 60 64" fill="none" stroke="#fff" stroke-width="2"><circle cx="30" cy="16" r="6"/><path d="M20 32a10 10 0 0 1 20 0z"/><circle cx="14" cy="40" r="5"/><circle cx="46" cy="40" r="5"/><path d="M4 58a10 10 0 0 1 20 0zM36 58a10 10 0 0 1 20 0z"/></svg>
    <div class="divider"></div>
    <h3>EXCELLENT TEAM</h3>
    <p>Lorem Ipsum is simply dummy text of the printing and typesetting industry. Lorem Ipsum has been.</p>
    <a class="more" href="#"><span>LEARN MORE</span></a>
  </article>
  <article class="service-card" style="left:766px;top:1930px">
    <svg class="icon" viewBox="0 0 60 64" fill="none" stroke="#fff" stroke-width="2"><circle cx="34" cy="22" r="13"/><circle cx="34" cy="22" r="6"/><rect x="6" y="40" width="8" height="16"/><path d="M14 52h16l18-10"/></svg>
    <div class="divider"></div>
    <h3>SUPPORT</h3>
    <p>Lorem Ipsum is simply dummy text of the printing and typesetting industry. Lorem Ipsum has been.</p>
    <a class="more" href="#"><span>LEARN MORE</span></a>
  </article>
</section>

<section class="team">
  <h2 class="section-title" style="top:2462px">OUR <strong>TEAM</strong></h2>
  <div class="title-rule"></div>
  <div class="team-text">
    <p>Lorem Ipsum is simply dummy text of the printing and typesetting industry. Lorem Ipsum has been.</p>
    <p>Lorem Ipsum is simply dummy text of the printing and typesetting industry. Lorem Ipsum has been.</p>
    <p>Lorem Ipsum is simply dummy text of the printing and typesetting industry. Lorem Ipsum has been.</p>
    <p>Lorem Ipsum is simply dummy text</p>
  </div>
  <div class="team-photo" role="img" aria-label="Portrait of a team member in a light blue shirt" style="background:radial-gradient(circle at 50% 40%,#eef1f6,#c7d0de)"></div>
</section>

<section class="contact">
  <div class="photo" role="img" aria-label="Colleagues looking at a laptop, tinted blue" style="left:150px;top:2858px;width:427px;height:355px;background:linear-gradient(135deg,#3a5c8c,#1f3c68 60%,#2d4f80)"></div>
  <div class="contact-card"></div>
  <h2 class="contact-title">GET IN <strong>TOUCH</strong></h2>
  <div class="consent-box"></div>
  <p class="consent">I have read the data protection declaration and I agree that the data I have provided can be collected and stored electronically. My data will only be used for the sole purpose of processing and responding to my request. By sending the contact form, I agree to the processing of my data.</p>

  <div class="field">
    <label style="left:462px;top:3083px">FIRST NAME<sup>*</sup></label>
    <span class="val" style="left:462px;top:3107px">Jordan</span>
    <div class="rule" style="left:410px;top:3139px;width:252px"></div>
    <label style="left:763px;top:3083px">LAST NAME<sup>*</sup></label>
    <span class="val" style="left:763px;top:3107px">Reed</span>
    <div class="rule" style="left:709px;top:3139px;width:251px"></div>
  </div>
  <div class="field">
    <label style="left:462px;top:3157px">EMAIL ADDRESS<sup>*</sup></label>
    <span class="val" style="left:462px;top:3181px">jordanreed@mail.example</span>
    <div class="rule" style="left:410px;top:3213px;width:252px"></div>
    <label style="left:763px;top:3157px">PHONE<sup>*</sup></label>
    <span class="val" style="left:763px;top:3181px">123-456-7890</span>
    <div class="rule" style="left:709px;top:3213px;width:251px"></div>
  </div>
  <div class="field">
    <label style="left:462px;top:3230px">COMPANY NAME</label>
    <span class="val" style="left:462px;top:3254px">Company Name</span>
    <div class="rule" style="left:410px;top:3286px;width:550px"></div>
  </div>
  <div class="field">
    <label style="left:462px;top:3305px">MESSAGE</label>
    <span class="val" style="left:462px;top:3328px">Hi, do you have a moment to talk abo...]</span>
    <div class="rule" style="left:410px;top:3383px;width:500px"></div>
  </div>
  <a class="send-btn" href="#" aria-label="Send">
    <svg width="62" height="62" viewBox="0 0 62 62"><path d="M20 31l22-10-8 22-4-8z" fill="#fff"/><path d="M30 35l12-14" stroke="var(--navy)" stroke-width="1.5"/></svg>
  </a>
</section>

<footer class="footer">
  <svg width="1200" height="359" viewBox="0 0 1200 359" style="position:absolute;left:0;top:0">
    <polygon points="0,10 1200,10 1200,359 0,359" fill="var(--dark)"/>
    <polygon points="0,0 1200,0 1200,10 0,10" fill="#fff"/>
    <polygon points="650,69 1200,10 1200,118" fill="var(--navy)"/>
  </svg>
  <p class="footer-brand">TORVIK CONSULTING</p>
</footer>
<nav class="footer-nav">
  <a href="#" style="left:430px">Home</a>
  <a href="#" style="left:510px">About</a>
  <a href="#" style="left:592px">Services</a>
  <a href="#" style="left:688px">Contact Us</a>
</nav>
<p class="copyright">© 2021 Torvik Consulting. All Rights Reserved.</p>
<a class="social" href="#" aria-label="Social profile" style="left:524px"></a>
<a class="social" href="#" aria-label="Social profile" style="left:561px"></a>
<a class="social" href="#" aria-label="Social profile" style="left:597px"></a>
<a class="social" href="#" aria-label="Social profile" style="left:634px"></a>
<p class="legal">Management Consulting<span>|</span>PrivacyPolicy</p>

</body>
</html>
```